Corporate ID design for Financial Services/Accountant Company - brochure, flyer, letterhead, email s

Hi designers :)

Torvela Financial Services requires a corporate ID design look and feel for all their ongoing items moving forward. It needs to be highly professional looking, corporate, contemporary and a standout design!

Items needed:
Letterhead design + follow-on header for 2nd and 3rd pages etc.
Tri-fold (or similar) brochure design
Flyer (A5) for mailout
Client form design
Email Signature Design

A boutique financial management company providing services in: Accounting, Bookkeeping, Payroll, Consulting services to corporate small & large clientele in Australia. The design needs to run across all items, matching them together to communicate professionalism, finance and style.

Logo needs to be on all items, however the design across all items can be completely different as long as it works in the logo (i.e don't want footprints over whole designs as it doesn't communicate hi-end corporate feel).

Would like a beautifully designed graphic element/design style included across all items to match together and become part of the corporate identity/branding.

Fresh, clean, modern, corporate and professional style.

ITEMS - how they will be used>
Letterhead - Will be used mainly online so design needs to be able to go into WORD document to edit over.

A5 flyer - will be printed on high gloss card. Needs to be double sided full colour for print with 3mm bleed

Tri-fold brochure - will be printed as well, needs to be standard print size, full cmyk colour both sides and it will be handed out to new clients for more information on prices & staff etc

Email signature - Just a nice simple and clean design with matching element from above items.

Client Form - needs to be laid out with a nice design in indesign please.

Thanks & look forward to your submissions!

Target Market(s)

Target market is professional businesses wanting financial and bookkeeping services delivered with exceptional service.

Industry/Entity Type

Financial

Requirements
Must have
• Logo
• Work in corporate/logo colours.
• Would like final files created in indesign if possible please. Graphics and illustration are fine in illustrator first.
• Design with some or a element from website to match everything together>
• http://www.torvela.com.au/
Nice to have
• Would love to see some designs in the blue, with creative designs/illustrations in background watermark (i.e opacity of grey showing a hint of a design across all items)
• Could work in the orange from website text if it looks good on some areas.
Should not have
• Don't want footprints over all items as the whole design. We want a new creative look and feel (corporate & professional) but just working in the logo. Can include PARTS of the footprint &/or logo in design across items.

```html
<!DOCTYPE html>
<html lang="en">
<head>
<meta charset="utf-8">
<title>Torvela Financial Services – Company &amp; Services</title>
<link href="https://fonts.googleapis.com/css2?family=PT+Serif:wght@400;700&family=Source+Sans+3:wght@600&display=swap" rel="stylesheet">
<style>
  :root {
    --paper: #ffffff;
    --heading: #5a5a5a;
    --body: #3a3a3a;
    --brand-blue: #2f8fc9;
    --badge-red: #c8202b;
    --badge-grey: #a6a6a6;
    --badge-light: #d9d9d9;
    --badge-blue: #1aa3dc;
    --badge-navy: #3a2f8c;
    --badge-orange: #e4572e;
    --badge-maroon: #b13a3a;
  }
  * { margin: 0; padding: 0; box-sizing: border-box; }
  html, body { width: 1200px; height: 847px; overflow: hidden; background: var(--paper); }
  .sheet { position: relative; width: 1200px; height: 847px; font-family: "PT Serif", Georgia, serif; color: var(--body); }
  .section-title { position: absolute; font-family: "Source Sans 3", Arial, sans-serif; font-weight: 600; font-size: 35px; color: var(--heading); top: 24px; }
  .company-title { left: 36px; }
  .services-title { left: 680px; }
  .company-copy { position: absolute; left: 36px; top: 86px; width: 558px; font-size: 21.5px; line-height: 29.5px; letter-spacing: 0.2px; text-align: justify; }
  .company-copy p { margin-bottom: 19px; }
  .closing { font-weight: 700; }
  .brand { position: absolute; left: 36px; top: 562px; display: flex; align-items: center; gap: 12px; }
  .brand-name { font-size: 30px; color: var(--heading); letter-spacing: 1px; }
  .brand-dot { width: 16px; height: 16px; border-radius: 50%; background: var(--brand-blue); }
  .contact { position: absolute; left: 36px; top: 656px; font-size: 19px; line-height: 24px; border-collapse: collapse; }
  .contact th { text-align: left; font-weight: 700; vertical-align: top; padding-right: 12px; white-space: nowrap; }
  .services-list { position: absolute; left: 680px; top: 80px; list-style: none; font-size: 22px; line-height: 37px; }
  .services-list li { display: flex; align-items: center; gap: 14px; }
  .services-list svg { width: 22px; height: 22px; flex: none; }
  .badges { position: absolute; left: 680px; top: 366px; width: 420px; height: 190px; }
  .hero-image { position: absolute; left: 580px; top: 560px; width: 620px; height: 287px;
    background: radial-gradient(ellipse at 55% 75%, #c9c2b0 0%, #dedad0 40%, #f1efe9 65%, var(--paper) 85%); }
</style>
</head>
<body>
<main class="sheet">
  <h2 class="section-title company-title">Our Company</h2>
  <div class="company-copy">
    <p>Torvela Financial Services is a boutique accountancy practice, providing tailor made financial solutions for small-to-medium size businesses throughout Sydney.</p>
    <p>Owned and run by a qualified and highly experienced Chartered Accountant, we offer a unique alternative to traditional accountancy and bookkeeping services. Abusiness objectives.</p>
    <p>Visit our website for more information or call us to find out just some of the reasons why your business can benefit from utilizing the services of an external accountant.</p>
    <p class="closing">We look forward to hearing from you!</p>
  </div>

  <div class="brand">
    <span class="brand-name">Torvela Financial Services</span>
    <span class="brand-dot"></span>
  </div>

  <table class="contact">
    <tr><th>Address:</th><td>Suite 7, Level 2, 118 Harbour Street<br>Marlow Bay, NSW 2098</td></tr>
    <tr><th>Office:</th><td>02 9100 4417</td></tr>
    <tr><th>Mobile:</th><td>0400 123 456</td></tr>
    <tr><th>Email:</th><td>admin@torvela.com.au</td></tr>
    <tr><th>Website:</th><td>www.torvela.com.au</td></tr>
  </table>

  <h2 class="section-title services-title">Our Services</h2>
  <ul class="services-list">
    <li><svg viewBox="0 0 22 22"><path d="M2 12 L8 18 L20 3" fill="none" stroke="#3a3a3a" stroke-width="3"/></svg>Bookkeeping</li>
    <li><svg viewBox="0 0 22 22"><path d="M2 12 L8 18 L20 3" fill="none" stroke="#3a3a3a" stroke-width="3"/></svg>Annual Accounts Preparation</li>
    <li><svg viewBox="0 0 22 22"><path d="M2 12 L8 18 L20 3" fill="none" stroke="#3a3a3a" stroke-width="3"/></svg>Tax Returns</li>
    <li><svg viewBox="0 0 22 22"><path d="M2 12 L8 18 L20 3" fill="none" stroke="#3a3a3a" stroke-width="3"/></svg>Part-time Financial Controller / CFO</li>
    <li><svg viewBox="0 0 22 22"><path d="M2 12 L8 18 L20 3" fill="none" stroke="#3a3a3a" stroke-width="3"/></svg>Zentallo, Fivrak &amp; Quonder</li>
    <li><svg viewBox="0 0 22 22"><path d="M2 12 L8 18 L20 3" fill="none" stroke="#3a3a3a" stroke-width="3"/></svg>Company Setups &amp; Registration</li>
  </ul>

  <svg class="badges" viewBox="0 0 420 190" role="img" aria-label="Professional membership and software partner badges">
    <circle cx="34" cy="34" r="30" fill="var(--badge-red)"/>
    <rect x="76" y="14" width="130" height="40" fill="var(--badge-light)"/>
    <rect x="6" y="104" width="50" height="56" fill="var(--badge-maroon)"/>
    <rect x="100" y="112" width="44" height="44" fill="var(--badge-orange)" transform="rotate(45 122 134)"/>
    <circle cx="278" cy="56" r="34" fill="var(--badge-blue)"/>
    <circle cx="350" cy="56" r="34" fill="var(--badge-grey)"/>
    <rect x="234" y="118" width="86" height="30" rx="4" fill="var(--badge-navy)"/>
    <rect x="328" y="118" width="86" height="30" rx="4" fill="var(--badge-red)"/>
  </svg>

  <div class="hero-image" role="img" aria-label="Pile of coins with a young green plant sprouting from them"></div>
</main>
</body>
</html>
```